Business card for real estate agent / office

We're looking for a new business card. We want something that is pretty clean, modern and sleek. Something that also tells people that we are a new age company...cutting edge. Although real estate has been done a certain way the last 100 years, we have energy and vibrance. Company name is Silver Meadow Properties. info can be found here: http://www.smprealtyhub.example/

needs to include: Name, title, phone number, email. our license number also needs to be displayed somewhere.

Target Market(s)

25-55 homeowners or potential homeowners

Industry/Entity Type

Business

Contact Information for Business Card

we need business card designs for real estate agent / office

Font styles to use
Serif

Requirements
Must have
• needs to include: Name, title, phone number, email. our license number also needs to be displayed somewhere and company name.
Nice to have
• placement area for photo

```html
<!DOCTYPE html>
<html lang="en">
<head>
<meta charset="utf-8">
<title>Silver Meadow Properties – Business Card</title>
<link rel="stylesheet" href="https://fonts.googleapis.com/css2?family=Open+Sans:ital,wght@0,400;0,600;0,700;1,400&display=swap">
<style>
  :root {
    --stage: #0b0b0b;
    --paper: #fbf9f5;
    --navy: #134a6b;
    --navy-deep: #0f4463;
    --green: #5db848;
    --ink: #4a4a4a;
    --white: #ffffff;
  }
  * { box-sizing: border-box; margin: 0; padding: 0; }
  html, body {
    width: 1200px; height: 1000px; overflow: hidden;
    background: var(--stage);
    font-family: "Open Sans", Arial, sans-serif;
  }
  .stage { position: relative; width: 1200px; height: 1000px; }
  .card {
    position: absolute; top: 357px;
    width: 500px; height: 286px;
    background: var(--paper);
    border-radius: 16px;
    overflow: hidden;
    box-shadow: 0 6px 18px rgba(0,0,0,.6);
  }
  .card--front { left: 70px; }
  .card--back { left: 630px; }

  .brand-name {
    position: absolute;
    color: var(--navy);
    font-weight: 700;
    line-height: 1.05;
  }
  .card--front .brand-name {
    left: 70px; top: 78px; width: 150px; font-size: 22px;
  }
  .photo-note {
    position: absolute; left: 290px; top: 128px;
    color: var(--navy); font-size: 19px; font-style: italic;
  }

  .card--back .brand-name {
    left: 34px; top: 60px; width: 200px; font-size: 24px;
  }
  .wave { position: absolute; left: 0; top: 0; width: 500px; height: 286px; }

  .agent { position: absolute; left: 282px; top: 44px; width: 205px; }
  .agent-name { color: var(--navy); font-weight: 700; font-size: 19px; }
  .agent-title { color: var(--ink); font-size: 12.5px; margin-top: 1px; white-space: nowrap; }

  .contact { position: absolute; left: 282px; top: 104px; width: 205px; list-style: none; }
  .contact li {
    display: flex; align-items: center; gap: 7px;
    color: var(--ink); font-size: 13px; line-height: 19px;
    white-space: nowrap;
  }
  .contact svg { width: 12px; height: 12px; flex: none; }

  .license {
    position: absolute; left: 46px; top: 214px;
    color: var(--white); font-size: 14px; letter-spacing: .3px;
  }
</style>
</head>
<body>
<main class="stage">

  <section class="card card--front" aria-label="Card front">
    <div class="brand-name">Silver Meadow Properties</div>
    <p class="photo-note">Place for Picture</p>
  </section>

  <section class="card card--back" aria-label="Card back">
    <svg class="wave" viewBox="0 0 500 286" aria-hidden="true">
      <path fill="var(--green)" d="M0,150 C120,128 210,150 270,200 C330,250 420,240 500,190 L500,220 C420,262 320,268 262,222 C205,176 120,160 0,176 Z"/>
      <path fill="var(--navy-deep)" d="M0,176 C120,160 205,176 262,222 C320,268 420,262 500,220 L500,286 L0,286 Z"/>
      <path fill="none" stroke="var(--paper)" stroke-width="3" d="M0,174 C120,158 205,174 262,220 C320,266 420,260 500,218"/>
    </svg>

    <div class="brand-name">Silver Meadow Properties</div>

    <div class="agent">
      <h1 class="agent-name">Daniel Harlow</h1>
      <p class="agent-title">Real Estate Broker, Realtor, MBA</p>
    </div>

    <ul class="contact">
      <li>
        <svg viewBox="0 0 12 12"><rect x="3" y="0.5" width="6" height="11" rx="1.2" fill="none" stroke="var(--green)" stroke-width="1.3"/><circle cx="6" cy="9.5" r=".8" fill="var(--green)"/></svg>
        555.214.3890
      </li>
      <li>
        <svg viewBox="0 0 12 12"><rect x="0.5" y="2" width="11" height="8" fill="var(--green)"/><path d="M0.5,2 L6,6.5 L11.5,2" fill="none" stroke="var(--paper)" stroke-width="1"/></svg>
        dan@smprealtyhub.example
      </li>
      <li>
        <svg viewBox="0 0 12 12"><circle cx="6" cy="6" r="5.3" fill="none" stroke="var(--green)" stroke-width="1.3"/><ellipse cx="6" cy="6" rx="2.3" ry="5.3" fill="none" stroke="var(--green)" stroke-width="1"/><path d="M0.7,6 H11.3" stroke="var(--green)" stroke-width="1"/></svg>
        www.smprealtyhub.example
      </li>
    </ul>

    <p class="license">CA BRE #02459318</p>
  </section>

</main>
</body>
</html>
```